Dental Patient Education Single page-Multiple pages needed.

I am creating a unique dental patient education materials for resale. I work in the dental industry, training dentists and thier teams how to improve patient acceptance rates for treatment. I see a need that all patient education material is designed incorrectly. I want to fix this by creating patient education material that educated patients based on all of the treatment options for a diagnosed condition. Tradidional patient education material reads like a catalog of procedures. This format is not effective for helping the patient quickly understand the consequences of non treatment and the benefits and disadvantages of their treatment options. Specifics of the Job:The design images must be royalty free.I will provide the text.Initially there are for major diagnosed conditions: Infected Tooth Treatment Options, Single to Multiple Missing tooth Treatment Options, Full Arch of Missing Teeth Treatment Options, and Full Arch Fixed Dental Implant Treatment OptionsThe layout should mirror the attached sample of Single Missing Tooth Treatment Options.This is a project that will require edits and redesigned based on testing.I also need this in Adobe, so it can be customized/branded for a dental office.

Target Market(s)

Dental office professionals to educate patients.

Font styles to use
Sans Serif

Colors
3277b5

Requirements
Must have
• Professional look and feel
• Royalty free images
• Easy to read

```html
<!DOCTYPE html>
<html lang="en">
<head>
<meta charset="utf-8">
<title>Single Missing Tooth – Treatment Options</title>
<link href="https://fonts.googleapis.com/css2?family=Nunito:wght@400;600;700;800&display=swap" rel="stylesheet">
<style>
:root{
  --brand:#3277b5;
  --brand-dark:#1c5aa3;
  --brand-light:#2aa0dc;
  --ink:#1d1d1d;
  --paper:#ffffff;
  --stage:#e9ebee;
  --gum:#e39aa0;
  --xray:#4a5560;
}
*{margin:0;padding:0;box-sizing:border-box}
html,body{width:1200px;height:800px;overflow:hidden;background:var(--stage);font-family:'Nunito',sans-serif;color:var(--ink)}
.sheet{position:absolute;left:298px;top:10px;width:604px;height:780px;background:var(--paper);box-shadow:0 4px 18px rgba(0,0,0,.18);overflow:hidden;display:flex;flex-direction:column}
.sheet>*{flex-shrink:0}
.masthead{position:relative;height:88px;background:linear-gradient(90deg,var(--brand-light),var(--brand) 55%,var(--brand-dark));padding:14px 24px}
.masthead h1{color:#fff;font-weight:700;font-size:30px;line-height:1.1}
.masthead .subtitle{color:#dff0ff;font-weight:400;font-size:22px;line-height:1.25}
.office-mark{position:absolute;right:20px;top:22px;width:120px;height:28px;background:#fff}
.intro{padding:10px 24px 8px;font-size:14px;line-height:1.4}
.intro p+p{margin-top:5px}
.option{margin-top:8px}
.option:first-of-type{margin-top:0}
.option-band{height:24px;background:linear-gradient(90deg,var(--brand),var(--brand-dark));color:#fff;font-weight:800;font-size:15px;line-height:24px;padding-left:24px;white-space:nowrap}
.photo-row{display:flex;gap:8px;padding:8px 24px 0}
.photo{flex:1;height:88px}
.photo.xray{background:linear-gradient(135deg,#2b333c,var(--xray) 50%,#1e252c)}
.photo.mouth{background:linear-gradient(180deg,#3a2622,#8a5148 55%,#c98a86)}
.caption{padding:5px 24px 0;font-size:11px;line-height:1.35}
.option.split{display:grid;grid-template-columns:430px 1fr;column-gap:12px;padding-right:18px}
.option.split .option-band{grid-column:1;grid-row:1}
.option.split .body-copy{grid-column:1;grid-row:2;padding-left:24px}
.option.split .illustration{grid-column:2;grid-row:1 / 3}
.body-copy{padding-top:6px;font-size:11.5px;line-height:1.35}
.body-copy.small{font-size:11px}
.side-row{display:flex;gap:12px;padding:6px 18px 0 24px}
.side-row .illustration{width:170px;height:84px;flex-shrink:0}
.side-row .body-copy{padding-top:0}
.illustration{background:linear-gradient(180deg,var(--gum),#f3d6d6 60%,#fafafa)}
.footer-band{margin-top:auto;height:28px;background:linear-gradient(90deg,var(--brand-light),var(--brand) 50%,var(--brand-dark))}
</style>
</head>
<body>
<main class="sheet">
  <header class="masthead">
    <h1>Single Missing Tooth</h1>
    <div class="subtitle">You Option for Treament</div>
    <div class="office-mark"></div>
  </header>

  <section class="intro">
    <p>A missing tooth is a serious issue. It can cause long-term damage to facialstructure, bone density and your ability to feel confident in your smile.</p>
    <p>Harbor Lane Dental has several options available to fix your missing tooth.</p>
  </section>

  <section class="option">
    <h2 class="option-band">Option 1: Do Nothing</h2>
    <div class="photo-row">
      <div class="photo xray" role="img" aria-label="X-ray showing a gap from a missing tooth"></div>
      <div class="photo mouth" role="img" aria-label="Photo of a mouth with damaged and missing teeth"></div>
      <div class="photo xray" role="img" aria-label="X-ray showing teeth shifting into a gap"></div>
    </div>
    <p class="caption">If you choose to do nothing at this time, the cost down the road can be substantial. $10,000+ for orthodontics to straighten out the teeth, implant,abutment and crown, bone grafting and possible sinus lift to replace lost bone</p>
  </section>

  <section class="option split">
    <h2 class="option-band">Option 2: Dental Implant</h2>
    <p class="body-copy">The <b>bad</b> news is that a dental implant is the most expensive option, <b>BUT</b> the good news is it is the most effective, functional and aesthetically pleasing. A dental implant will keep the bone in that area of the jaw from atrophy. It helps maintain face shape and prevents 'sunken face'. The implant will prevent surrounding teeth from shifting and chances of losing the tooth decline. It will keep the teeth from shifting, and will prevent any future need to cut down the adjacent teeth. A dental implant is the nearest thing to a natural tooth available today.</p>
    <div class="illustration" role="img" aria-label="Illustration of a dental implant with abutment and crown"></div>
  </section>

  <section class="option">
    <h2 class="option-band">Option 2: Dental Bridge</h2>
    <div class="side-row">
      <div class="illustration" role="img" aria-label="Illustration of a three-unit dental bridge over prepared teeth"></div>
      <p class="body-copy small">The <b>good</b> news here is that a bridge is less expensive than the implant option <b>BUT</b> you will continue to lose bone in that area over time. Food will get caught in the hard to reach areas and if not cleaned properly could mean you have to replace the bridge every 7 years. In addition, to secure the bridge, the adjacent teeth must be cut down in order to be used as anchors for the appliance. Why cut down two good teeth if we don't have to?</p>
    </div>
  </section>

  <section class="option split">
    <h2 class="option-band">Option 2: The Removable Partial Denture (RPD)</h2>
    <p class="body-copy small">The <b>good</b> news here is that it's the least expensive option of the 3, but the <b>BAD</b> news is that your teeth have to come out every night. You won't be able to chew your food as well and your tongue will be uncomfortable with the big, bulky plastic sitting inyour mouth all day.</p>
    <div class="illustration" role="img" aria-label="Illustration of a removable partial denture with clasps"></div>
  </section>

  <div class="footer-band"></div>
</main>
</body>
</html>
```